Meurtre chez la Vern‘

“Vern’” is the informal nickname used inside the French police for the "Escouade Vernaleuse du Nord", an elite homicide unit. The apostrophe reflects spoken language and internal slang. The title Meurtre chez la Vern’ highlights the central irony of the novel: a murder committed inside the very place meant to investigate murders.
Summary
A woman’s body is found inside the offices of Paris’s elite homicide squad. As detectives investigate, they uncover buried cases, internal rivalries and institutional silence. The closer they get to the truth, the clearer it becomes: this crime was meant to stay hidden.
Keywords : Woman’s body, Police procedural, Murder inside the police, Elite homicide unit, Dark realism, 58 rue Bastelinou.
Size : 16 x 24 cm
Title : Meurtre chez la Vern'
Author : Lucien Maréchaux
Publisher : Editions Torvelle (at the bottom of the page)
Book

```html
<!DOCTYPE html>
<html lang="fr">
<head>
<meta charset="utf-8">
<title>Meurtre chez la Vern' — Lucien Maréchaux</title>
<link rel="stylesheet" href="https://fonts.googleapis.com/css2?family=Lato:wght@700;900&family=Kaushan+Script&display=swap">
<style>
  :root {
    --night: #07121b;
    --corridor: #13283a;
    --corridor-light: #4d6f86;
    --glow: #cfe0ea;
    --title-red: #ee3a4f;
    --paper: #ffffff;
    --muted: #c9d6df;
  }
  * { margin: 0; padding: 0; box-sizing: border-box; }
  html, body {
    width: 800px;
    height: 1200px;
    overflow: hidden;
    background: var(--night);
  }
  .cover {
    position: relative;
    width: 800px;
    height: 1200px;
    overflow: hidden;
    background: var(--night);
  }
  .cover-photo {
    position: absolute;
    inset: 0;
    background:
      radial-gradient(ellipse 90px 300px at 452px 670px, var(--glow) 0%, rgba(207,224,234,0.35) 45%, rgba(0,0,0,0) 100%),
      linear-gradient(160deg, rgba(0,0,0,0) 55%, rgba(120,150,170,0.25) 70%, rgba(0,0,0,0) 80%),
      radial-gradient(ellipse 300px 520px at 420px 660px, var(--corridor-light) 0%, var(--corridor) 45%, var(--night) 100%);
  }
  .title-block {
    position: absolute;
    inset: 0;
    font-weight: normal;
  }
  .title-word,
  .title-link {
    position: absolute;
    left: 0;
    width: 800px;
    text-align: center;
    white-space: nowrap;
  }
  .title-word {
    font-family: "Lato", sans-serif;
    font-weight: 900;
    color: var(--title-red);
    font-size: 140px;
    line-height: 1;
    letter-spacing: -2px;
  }
  .title-word--first { top: 136px; }
  .title-word--second { top: 350px; }
  .title-link {
    top: 282px;
    font-family: "Kaushan Script", cursive;
    color: var(--paper);
    font-size: 64px;
    line-height: 1;
  }
  .genre-tag {
    position: absolute;
    top: 514px;
    left: 155px;
    width: 130px;
    height: 34px;
    background: var(--paper);
    color: var(--title-red);
    font-family: "Lato", sans-serif;
    font-weight: 900;
    font-size: 26px;
    line-height: 34px;
    text-align: center;
    letter-spacing: 1px;
  }
  .author {
    position: absolute;
    top: 1038px;
    left: 0;
    width: 800px;
    text-align: center;
    font-family: "Lato", sans-serif;
    font-weight: 900;
    color: var(--paper);
    font-size: 60px;
    letter-spacing: 2px;
    line-height: 1;
    white-space: nowrap;
  }
  .publisher {
    position: absolute;
    top: 1138px;
    left: 0;
    width: 800px;
    text-align: center;
    font-family: "Lato", sans-serif;
    font-weight: 700;
    color: var(--muted);
    font-size: 18px;
    letter-spacing: 4px;
    line-height: 1;
    text-transform: uppercase;
  }
</style>
</head>
<body>
  <main class="cover">
    <div class="cover-photo" role="img" aria-label="Couloir sombre de bureaux de police, une porte entrouverte au fond laisse passer un faisceau de lumière sur le carrelage"></div>
    <h1 class="title-block">
      <span class="title-word title-word--first">MEURTRE</span>
      <span class="title-link">chez la</span>
      <span class="title-word title-word--second">VERN'</span>
    </h1>
    <p class="genre-tag">ROMAN</p>
    <p class="author">LUCIEN MARÉCHAUX</p>
    <p class="publisher">Editions Torvelle</p>
  </main>
</body>
</html>
```